Need help refining Tallbergsgillet

Hi We need help with the refining of overall design and details of our homepage design Tallbergsgillet. See attached files.

Attached files:
homepage.psd - file you can use to work from.
homepage.png – quick notes on thoughts of the design
logo.psd (smart object) – The logo should be in gold.
social media elements.png - what type of data that needs design in the feed

What we need:
Something is missing with the overall design as well as detailed design for our social media feed. We don’t know what and hope you can solve this for us.

The homepage:
Our main page include a selfloading blogfeed combined with Vendraly- and Instagramfeed.

Fonts:
So far I´ve used Roboto regular, and Georgia, but feel free to use other fonts if you find better suited

Among others, we need a better detailed design that works better with the overall design.

Se attached sample image (social_mediafeed.png) what types of data we get from Vendraly in our feed. Feel free to redesign the elements of this data.

Headerlinks:
Even though we only have one page, there should be place for links to other pages as well which will load below the header.

Social media follow: Place for social media follow links/icons/buttons in style with rest of the design. Maybe at top grey border? We use Glimtora and Vendraly in style with rest of the design.

Colors:
The logo should be in gold, and use of "goldish" colors troughout the page.
Also blue elements troughout the page

Logo in gold/goldish color
Blue elements # 13416c (or similar color that works well in the design)

Target Market(s)

Wellness, fitness, spa and food, Exclusive

Number of Pages Required

1 page

Font styles to use
Serif
Sans Serif
Script
Other font styles liked:
• Roboto, Georgia

Requirements
Must have
• Better overall design that feel harmonic.
• Better design of blog and social media feeds (se all attached images)
• Nice clean design, easy on the eye
• Colors on theme: Gold + blue

```html
<!DOCTYPE html>
<html lang="sv">
<head>
<meta charset="utf-8">
<title>Tallbergsgillet</title>
<link href="https://fonts.googleapis.com/css2?family=Playfair+Display:wght@400;700&family=Roboto:wght@300;400;500;700&display=swap" rel="stylesheet">
<style>
:root{
  --navy:#13416c;
  --navy-dark:#0c2540;
  --ink:#1d2a38;
  --gold:#c9a43a;
  --gold-light:#e2c46a;
  --grey-bg:#eeeeee;
  --line:#d8d8d8;
  --text:#555d66;
  --white:#ffffff;
}
*{box-sizing:border-box;margin:0;padding:0}
html,body{width:1200px;height:2224px;overflow:hidden}
body{font-family:"Roboto",sans-serif;color:var(--text);background:var(--white);font-size:14px}
.serif{font-family:"Playfair Display",serif}

/* top bar */
.topbar{height:32px;background:var(--navy-dark);display:flex;align-items:center;justify-content:space-between;padding:0 0 0 40px;color:#c9d3de;font-size:12px}
.topbar .contact{display:flex;gap:26px;align-items:center}
.topbar .contact span{display:flex;gap:6px;align-items:center}
.topbar .member{display:flex;height:32px}
.topbar .member a{display:flex;align-items:center;padding:0 22px;color:var(--white);text-decoration:none;font-size:11px;font-weight:500;letter-spacing:.5px;background:var(--gold)}
.topbar .member a.login{background:#a8862a}

/* nav */
.mainnav{height:108px;display:flex;align-items:center;justify-content:center;position:relative;border-bottom:1px solid var(--line)}
.mainnav ul{list-style:none;display:flex;gap:40px;font-size:13px;font-weight:500;letter-spacing:.6px;color:var(--ink)}
.mainnav .left{position:absolute;left:110px}
.mainnav .right{position:absolute;right:40px}
.logo{width:220px;height:108px;background:var(--navy);display:flex;flex-direction:column;align-items:center;justify-content:center;gap:8px}
.logo .mark{width:34px;height:34px;border-radius:50%;background:var(--gold)}
.logo .name{font-family:"Playfair Display",serif;color:var(--gold);font-size:17px;letter-spacing:1.5px}

/* hero */
.hero{height:520px;position:relative;overflow:hidden}
.hero .photo{position:absolute;inset:0;background:linear-gradient(180deg,#3c4d63 0%,#8a7a6a 38%,#e6b069 52%,#9e6b3c 64%,#2b2522 100%)}
.hero .arrow{position:absolute;top:230px;width:40px;height:60px;display:flex;align-items:center;justify-content:center}
.hero .arrow.prev{left:20px}.hero .arrow.next{right:20px}
.featured{position:absolute;right:60px;top:312px;width:324px;text-align:right;color:var(--white)}
.featured h2{display:inline-block;background:rgba(12,37,64,.75);font-family:"Playfair Display",serif;font-weight:400;font-size:40px;padding:6px 16px}
.featured p{display:inline-block;background:rgba(12,37,64,.75);font-size:16px;padding:6px 16px;margin-top:6px}
.featured .btn{margin-top:10px}
.dots{position:absolute;left:50%;bottom:20px;transform:translateX(-50%);display:flex;gap:8px}
.dots i{width:10px;height:10px;border-radius:50%;background:rgba(255,255,255,.5)}
.dots i.on{background:var(--white)}

.btn{display:inline-flex;align-items:center;gap:8px;height:34px;padding:0 22px;background:var(--navy);color:var(--white);font-size:12px;font-weight:500;letter-spacing:.6px}
.btn.gold{background:var(--gold)}

/* section heading */
.section-title{display:flex;align-items:center;justify-content:center;gap:22px}
.section-title::before,.section-title::after{content:"";width:150px;height:1px;background:var(--gold)}
.section-title h2{font-family:"Playfair Display",serif;font-weight:400;font-size:36px;letter-spacing:1px;color:var(--ink)}
.section-title h2 em{font-style:normal;color:var(--gold)}

/* offers */
.offers{height:490px;padding-top:44px}
.cards{display:flex;gap:20px;justify-content:center;margin-top:54px}
.card{width:250px}
.card .photo{height:190px;position:relative;background:linear-gradient(180deg,#2b3558 0%,#5d4a78 45%,#a06a6e 75%,#2a2330 100%)}
.card .photo .overlay{position:absolute;left:0;right:0;top:16px;background:rgba(193,38,58,.85);color:var(--white);padding:6px 12px}
.card .photo .overlay strong{display:block;font-family:"Playfair Display",serif;font-size:19px;font-weight:400}
.card .photo .overlay span{font-size:12px}
.badge{position:absolute;right:10px;bottom:-22px;width:80px;height:88px;clip-path:polygon(50% 0,100% 25%,100% 75%,50% 100%,0 75%,0 25%);background:var(--navy);color:var(--white);display:flex;flex-direction:column;align-items:center;justify-content:center;line-height:1}
.badge b{font-size:24px;color:var(--gold-light)}
.badge small{font-size:11px;font-weight:700;margin-top:3px}
.badge.gold{background:var(--gold)}
.badge.gold b{color:var(--white)}
.card h3{font-family:"Playfair Display",serif;font-size:20px;color:var(--navy);margin-top:16px;letter-spacing:.5px}
.card p{font-size:12px;margin:4px 0 14px}

/* blog */
.blog{height:510px;background:var(--grey-bg);padding-top:40px}
.post{display:flex;gap:36px;margin:52px 0 0 100px}
.post .photo{width:500px;height:300px;background:linear-gradient(180deg,#e4c89a 0%,#f0d8a8 40%,#b98a55 70%,#5a4330 100%)}
.post .body{width:460px}
.post .head{display:flex;gap:14px;align-items:flex-start}
.date{display:flex;gap:6px;align-items:flex-start;color:var(--gold)}
.date b{font-family:"Playfair Display",serif;font-size:48px;font-weight:400;line-height:1}
.date span{font-size:12px;line-height:1.2;margin-top:6px}
.post h3{font-family:"Playfair Display",serif;font-weight:400;font-size:30px;color:var(--ink);line-height:1.15}
.meta{display:flex;gap:22px;font-size:10px;color:#8a929a;margin:14px 0 14px 100px;letter-spacing:.4px}
.post p.excerpt{font-size:13px;line-height:1.55;margin-left:100px}
.actions{display:flex;gap:8px;margin:28px 0 0 100px}

/* feeds */
.feeds{height:520px;padding:60px 100px 0}
.feed{border:1px solid var(--line)}
.feed+.feed{margin-top:40px}
.feed .bar{height:34px;background:var(--navy);display:flex;align-items:center;justify-content:space-between;padding:0 14px;color:var(--white);font-size:12px}
.feed .bar .brand{font-weight:700;font-size:14px}
.feed .item{display:flex;gap:14px;padding:14px;border-bottom:1px solid var(--line)}
.feed .item:last-child{border-bottom:0}
.avatar{width:40px;height:40px;background:linear-gradient(135deg,#6d7f93,#3b4b5e);flex:none}
.feed .item h4{font-size:13px;color:var(--ink);font-weight:500}
.feed .item .time{font-size:10px;color:#9aa1a8;margin:2px 0 6px}
.feed .item p{font-size:11px;line-height:1.5}
.thumb{width:120px;height:90px;background:linear-gradient(135deg,#c9d2dc,#7d8fa3);flex:none}
.feed .item .links{font-size:10px;color:var(--navy);margin-top:6px}

/* footer */
.footer{height:44px;background:var(--navy-dark);display:flex;align-items:center;justify-content:space-between;padding:0 40px;color:#aeb8c4;font-size:11px}
.footer .icons{display:flex;gap:10px}
.footer .icons i{width:24px;height:24px;border-radius:50%;background:var(--gold)}
</style>
</head>
<body>

<div class="topbar">
  <div class="contact">
    <span><svg width="12" height="12" viewBox="0 0 24 24"><path fill="#c9a43a" d="M6.6 10.8a15 15 0 0 0 6.6 6.6l2.2-2.2c.3-.3.7-.4 1-.2 1.1.4 2.3.6 3.6.6.6 0 1 .4 1 1V20c0 .6-.4 1-1 1A17 17 0 0 1 3 4c0-.6.4-1 1-1h3.5c.6 0 1 .4 1 1 0 1.3.2 2.5.6 3.6.1.3 0 .7-.2 1z"/></svg>(08) 555 0142</span>
    <span><svg width="12" height="12" viewBox="0 0 24 24"><path fill="#c9a43a" d="M3 5h18v14H3zm2 2v.5l7 4.5 7-4.5V7z"/></svg>info@tallbergsgillet.se</span>
  </div>
  <div class="member"><a>BLI MEDLEM</a><a class="login">MEDLEMSLOGIN</a></div>
</div>

<nav class="mainnav">
  <ul class="left"><li>LIVSBLOGGEN</li><li>INSPIRATION</li></ul>
  <div class="logo"><span class="mark"></span><span class="name">TALLBERGSGILLET</span></div>
  <ul class="right"><li>MEDLEMSERBJUDANDEN</li><li>OM ▾</li><li>KONTAKTA OSS</li></ul>
</nav>

<section class="hero">
  <div class="photo" role="img" aria-label="Fotografi av en löpare i motljus på en brygga vid havet i solnedgång"></div>
  <div class="arrow prev"><svg width="20" height="40" viewBox="0 0 20 40"><path d="M18 2 2 20l16 18" fill="none" stroke="#fff" stroke-width="2.5"/></svg></div>
  <div class="arrow next"><svg width="20" height="40" viewBox="0 0 20 40"><path d="M2 2l16 18L2 38" fill="none" stroke="#fff" stroke-width="2.5"/></svg></div>
  <div class="featured">
    <h2>Featured Post</h2><br>
    <p>Skön beskrivning av inlägget</p><br>
    <span class="btn">LÄS MER</span>
  </div>
  <div class="dots"><i></i><i class="on"></i><i></i></div>
</section>

<section class="offers">
  <div class="section-title"><h2>TALLBERGSGILLETS <em>MEDLEMSERBJUDANDEN</em></h2></div>
  <div class="cards">
    <article class="card">
      <div class="photo" role="img" aria-label="Fotografi av en stadssiluett i skymning">
        <div class="overlay"><strong>Ljusbadet AB</strong><span>Motionera mera</span></div>
        <div class="badge"><b>30%</b><small>RABATT!</small></div>
      </div>
      <h3>LJUSBADET AB</h3>
      <p>En kort rubrik på erbjudandet</p>
      <span class="btn">LÄS MER</span>
    </article>
    <article class="card">
      <div class="photo" role="img" aria-label="Fotografi av en stadssiluett i skymning">
        <div class="overlay"><strong>Ljusbadet AB</strong><span>Motionera mera</span></div>
        <div class="badge gold"><b>30%</b><small>RABATT!</small></div>
      </div>
      <h3>LJUSBADET AB</h3>
      <p>En kort rubrik på erbjudandet</p>
      <span class="btn gold">LÄS MER</span>
    </article>
    <article class="card">
      <div class="photo" role="img" aria-label="Fotografi av en stadssiluett i skymning">
        <div class="overlay"><strong>Ljusbadet AB</strong><span>Motionera mera</span></div>
        <div class="badge"><b>30%</b><small>RABATT!</small></div>
      </div>
      <h3>LJUSBADET AB</h3>
      <p>En kort rubrik på erbjudandet</p>
      <span class="btn">LÄS MER</span>
    </article>
  </div>
</section>

<section class="blog">
  <div class="section-title"><h2>SENASTE <em>BLOG</em></h2></div>
  <article class="post">
    <div class="photo" role="img" aria-label="Fotografi av en kvinna som springer på en väg i varmt morgonljus"></div>
    <div class="body">
      <div class="head">
        <div class="date"><b>22</b><span>OKTOBER<br>2016</span></div>
      </div>
      <h3 style="margin:-44px 0 0 100px">eleifend nibh et ultricies justo Vivamus .</h3>
      <div class="meta"><span>AV ANNA LINDBERG</span><span>3 KOMMENTARER</span><span>HÄLSA</span></div>
      <p class="excerpt">Ad hoc consectetur, eleifend nibh et, ultricies justo. Vivamus luctus nisl ut lacus placerat laoreet sed ut lacus. Sed a molestie ex. Donec ultricies nisl eu mollis tristique, ut ornare lorem.</p>
      <p class="excerpt" style="margin-top:10px">Nulla felis sem, condimentum fermentum ullamcorper.</p>
      <div class="actions">
        <span class="btn"><svg width="12" height="12" viewBox="0 0 24 24"><path fill="#fff" d="M18 16a3 3 0 0 0-2 .8L8.9 12.7a3 3 0 0 0 0-1.4L16 7.2A3 3 0 1 0 15 5v.3L7.9 9.4a3 3 0 1 0 0 5.2l7.1 4.1V19a3 3 0 1 0 3-3z"/></svg>DELA</span>
        <span class="btn"><svg width="12" height="12" viewBox="0 0 24 24"><path fill="#fff" d="M3 4h18v12H7l-4 4z"/></svg>KOMMENTERA</span>
        <span class="btn gold">LÄS MER</span>
      </div>
    </div>
  </article>
</section>

<section class="feeds">
  <div class="feed">
    <div class="bar"><span>Följ oss på Vendraly</span><span class="brand">Vendraly</span></div>
    <div class="item">
      <div class="avatar" role="img" aria-label="Profilbild"></div>
      <div>
        <h4>Quisque laoreet dui purus. Suspendisse sit amet nulla dolor.</h4>
        <div class="time">för 2 timmar sedan</div>
        <p>Ad hoc consectetur, eleifend nibh et, ultricies justo. Vivamus luctus nisl ut lacus placerat laoreet sed ut lacus. Sed a molestie ex. Donec ultricies nisl eu mollis tristique, ut ornare lorem ipsum dolor sit amet.</p>
      </div>
    </div>
    <div class="item">
      <div class="avatar" role="img" aria-label="Profilbild"></div>
      <div>
        <h4>Quisque laoreet dui purus. Suspendisse sit amet nulla dolor.</h4>
        <div class="time">igår</div>
      </div>
    </div>
  </div>
  <div class="feed">
    <div class="bar"><span>Följ oss på Glimtora</span><span class="brand">Glimtora</span></div>
    <div class="item">
      <div class="thumb" role="img" aria-label="Fotografi från gillets senaste träff"></div>
      <div>
        <h4>Quisque laoreet dui purus. Suspendisse sit amet nulla dolor.</h4>
        <div class="time">för 1 dag sedan</div>
        <p>Ad hoc consectetur, eleifend nibh et, ultricies justo. Vivamus luctus nisl ut lacus placerat laoreet sed ut lacus. Sed a molestie ex. Donec ultricies nisl eu mollis tristique.</p>
        <div class="links">GILLA · KOMMENTERA · DELA</div>
      </div>
    </div>
  </div>
</section>

<footer class="footer">
  <span>Copyright 2016 Tallbergsgillet. All Rights Reserved.</span>
  <div class="icons"><i></i><i></i><i></i><i></i></div>
</footer>

</body>
</html>
```